Disability Service Provider Expo Banner that will stand out amongst the competition

We would like to have a two banners designed to be able to display at expos that outline the services that we provide as a company. We are a disability service provider who aims to provider services to increase the independence of those living with a disability. We would like the banners to follow consistent themes/designs from other marketing material that we have (see brief for designs). One of the banners will be for the allied health services we provide (exercise physiology and occupational therapy) and the other banner will be promoting the our support worker, programs, and short-term accommodation. Our main colour schemes for therapy are black, yellow, and white. For our other services we utilise yellow, blue, and magenta as part of our colour pallet. Please utilise the information from the flyers, colours, and logos all located in the design brief. The style of banner can be seen in the images upload in the brief.

Target Market(s)

Parents and carers of those who livce with a disability, and seeking their business over our competitors

Industry/Entity Type

Disability Service and Health Provider

Colors

Designer to choose colors to be used in the design.

Requirements
Must have
• Eye catching, limited text
Nice to have
• Split services across a few banners
Should not have
• Lots of words

```html
<!DOCTYPE html>
<html lang="en">
<head>
<meta charset="utf-8">
<title>Brightvale Expo Banners</title>
<link rel="stylesheet" href="https://fonts.googleapis.com/css2?family=Montserrat:ital,wght@0,400;0,500;0,700;0,800;1,400&family=Crimson+Text:wght@700&family=Permanent+Marker&display=swap">
<style>
  :root {
    --stage: #9b9b9b;
    --black: #0b0b0b;
    --white: #ffffff;
    --yellow: #f2d424;
    --sun: #f7c948;
    --blue: #4f93d2;
    --magenta: #e8135f;
    --ink: #1a1a1a;
  }
  * { margin: 0; padding: 0; box-sizing: border-box; }
  html, body { width: 1200px; height: 1117px; overflow: hidden; }
  body { background: var(--stage); position: relative; font-family: "Montserrat", sans-serif; }

  .banner {
    position: absolute; top: 140px; width: 362px; height: 830px;
    background: var(--white); overflow: hidden;
    box-shadow: 0 18px 30px rgba(0,0,0,.25);
  }
  .banner--therapy { left: 195px; }
  .banner--support { left: 640px; }

  .shapes { position: absolute; inset: 0; width: 100%; height: 100%; }

  .brand {
    position: absolute; left: 0; right: 0; top: 48px; text-align: center; z-index: 2;
  }
  .brand__dot {
    display: block; width: 32px; height: 32px; border-radius: 50%;
    background: var(--sun); margin: 0 auto 12px;
  }
  .brand__name {
    font-family: "Montserrat", sans-serif; font-weight: 800;
    font-size: 33px; letter-spacing: -0.5px; line-height: 1;
    position: relative; left: -8px;
  }
  .banner--therapy .brand__name { color: var(--black); }
  .banner--support .brand__name { color: var(--white); }

  .headline { position: absolute; left: 20px; right: 20px; text-align: center; z-index: 2; }
  .banner--therapy .headline { top: 195px; }
  .banner--therapy .headline__title {
    font-weight: 800; font-size: 20px; line-height: 1.12; color: var(--white); text-transform: uppercase;
  }
  .headline__accent--yellow { color: var(--yellow); }
  .banner--therapy .headline__sub {
    margin-top: 10px; font-style: italic; font-size: 11.5px; line-height: 1.3; color: var(--white);
  }

  .banner--support .headline { top: 178px; left: 16px; right: 16px; }
  .banner--support .headline__title {
    font-family: "Crimson Text", serif; font-weight: 700; font-size: 19px; line-height: 1.08;
    color: var(--black); text-transform: uppercase;
  }
  .headline__accent--magenta { color: var(--magenta); }
  .banner--support .headline__sub {
    margin-top: 8px; font-style: italic; font-size: 11px; line-height: 1.22; color: var(--ink);
  }

  .photo { position: absolute; }
  .photo--group {
    left: 0; top: 318px; width: 348px; height: 278px;
    background: linear-gradient(160deg, #3f5a2e 0%, #7fa6cf 45%, #9ec3e6 70%, #4a5b72 100%);
    clip-path: polygon(0 10%, 100% 0, 100% 88%, 0 100%);
  }
  .photo--gym {
    left: 188px; top: 470px; width: 174px; height: 135px;
    background: linear-gradient(150deg, #dfe6ec 0%, #8fb6d1 50%, #2a3446 100%);
    clip-path: polygon(0 6%, 100% 0, 100% 92%, 0 100%);
    border: 3px solid var(--white);
  }
  .photo--craft {
    left: 0; top: 312px; width: 348px; height: 280px;
    background: linear-gradient(150deg, #cfdde8 0%, #9aa7b3 40%, #c7a38f 65%, #eef1f4 100%);
    clip-path: polygon(0 14%, 100% 0, 100% 88%, 0 100%);
  }
  .photo--friends {
    left: 194px; top: 470px; width: 168px; height: 132px;
    background: linear-gradient(150deg, #8f9a6e 0%, #5f6b57 45%, #2b3140 100%);
    clip-path: polygon(0 10%, 100% 0, 100% 90%, 0 100%);
  }

  .values {
    position: absolute; left: 24px; right: 24px; top: 626px;
    display: flex; justify-content: space-between; align-items: center;
    font-family: "Permanent Marker", cursive; font-size: 11px; color: var(--black);
    text-transform: uppercase; letter-spacing: .3px;
  }
  .banner--support .values { top: 614px; }
  .values__dot { width: 14px; height: 14px; border-radius: 50%; background: var(--sun); }

  .about {
    position: absolute; left: 30px; right: 30px; text-align: center;
    font-size: 9.6px; line-height: 1.28; color: var(--ink);
  }
  .banner--therapy .about { top: 658px; }
  .banner--support .about { top: 644px; }

  .site {
    position: absolute; left: 0; right: 0; bottom: 32px; text-align: center;
    font-weight: 700; font-size: 16px; color: var(--white);
  }
  .site__name { color: var(--yellow); }
</style>
</head>
<body>

  <section class="banner banner--therapy">
    <svg class="shapes" viewBox="0 0 362 830" preserveAspectRatio="none" aria-hidden="true">
      <polygon points="362,0 362,110 318,108" fill="var(--yellow)"/>
      <path d="M0,182 L290,140 Q312,136 318,108 L362,110 L362,330 L0,330 Z" fill="var(--black)"/>
      <polygon points="0,318 110,318 0,340" fill="var(--yellow)"/>
      <path d="M0,748 L300,775 Q340,780 362,830 L0,830 Z" fill="var(--black)"/>
    </svg>

    <div class="brand">
      <span class="brand__dot"></span>
      <div class="brand__name">BRIGHTVALE</div>
    </div>

    <div class="headline">
      <h1 class="headline__title"><span class="headline__accent--yellow">Exercise Physiology</span><br>and Occupational<br>Therapy</h1>
      <p class="headline__sub">Improve your health, quality of life,<br>and independence with the help of our<br>Exercise Physiologist!</p>
    </div>

    <div class="photo photo--group" role="img" aria-label="Photo: a group of smiling young people in blue shirts joining hands outdoors"></div>
    <div class="photo photo--gym" role="img" aria-label="Photo: an exercise physiologist guiding a client through floor exercise in a gym"></div>

    <div class="values">
      <span>More Independence</span><span class="values__dot"></span>
      <span>More Choice</span><span class="values__dot"></span>
      <span>More Fun</span>
    </div>

    <p class="about">At Brightvale, we believe that every person should have the opportunity to live an active, happy, and full life. For some, this can be limited by their physical or mental health and be tough to overcome on their own. With the help of our exercise physiologists, we can assist you to achieve your health and well-being and independence goals.</p>

    <p class="site">www.<span class="site__name">brightvale</span>.com.au</p>
  </section>

  <section class="banner banner--support">
    <svg class="shapes" viewBox="0 0 362 830" preserveAspectRatio="none" aria-hidden="true">
      <path d="M0,0 L362,0 L362,10 Q330,100 310,140 Q300,158 280,160 L0,170 Z" fill="var(--blue)"/>
      <polygon points="362,10 362,112 322,108" fill="var(--magenta)"/>
      <polygon points="0,300 160,300 0,330" fill="var(--yellow)"/>
      <path d="M0,758 L330,774 Q352,776 362,830 L0,830 Z" fill="var(--magenta)"/>
    </svg>

    <div class="brand">
      <span class="brand__dot"></span>
      <div class="brand__name">BRIGHTVALE</div>
    </div>

    <div class="headline">
      <h1 class="headline__title"><span class="headline__accent--magenta">Our Support Worker,</span><br>Programs, and Short-Term<br>Accommodation.</h1>
      <p class="headline__sub">Supporting you to develop independence.<br>Helping you to engage in community, social &amp;<br>recreational activities.</p>
    </div>

    <div class="photo photo--craft" role="img" aria-label="Photo: a young woman and a support worker doing a craft activity together at a table"></div>
    <div class="photo photo--friends" role="img" aria-label="Photo: three friends using wheelchairs together outdoors"></div>

    <div class="values">
      <span>More Independence</span><span class="values__dot"></span>
      <span>More Choice</span><span class="values__dot"></span>
      <span>More Fun</span>
    </div>

    <p class="about">We have a team who is experienced, passionate, dedicated &amp; FUN! We enjoy finding ways to provide social, recreational &amp; community participation opportunities for young people with mild to moderate disabilities &amp; mental health conditions. Our unique, real-life experiences are specifically tailored for this age group &amp; promote capacity building in a fun, safe, supportive, &amp; age-appropriate setting. We find that this approach strengthens social connection, confidence &amp; inclusion.</p>

    <p class="site">www.<span class="site__name">brightvale</span>.com.au</p>
  </section>

</body>
</html>
```